PRK website

Im a Specialty contractor that specializes in fireproofing. Epoxy flooring and terrazo along with poured floors and polished concrete.

We also do fire caulking.

Im the largest specialty flooring healthcare contractor in the south east.

Otto

Contractor

```html
<!DOCTYPE html>
<html lang="en">
<head>
<meta charset="utf-8">
<title>PRK – Fireproofing &amp; Specialty Flooring</title>
<link href="https://fonts.googleapis.com/css2?family=Questrial&family=Carlito:wght@400;700&family=Open+Sans:ital,wght@0,400;0,600;0,700;1,700&display=swap" rel="stylesheet">
<style>
  :root{
    --white:#ffffff;
    --ink:#2f3142;
    --accent:#1b8fb3;
    --hero-band:#343647;
    --section:#e4e4e4;
    --card:#383845;
    --card-edge:#5a5a66;
    --button:#8a6c68;
    --footer:#353535;
    --footer-rule:#8c7a78;
    --footer-text:#e6e6e6;
    --muted:#8a8a8a;
    --field:#7f7f7f;
    --bar:#000000;
    --icon:#c9c9c9;
  }
  *{box-sizing:border-box;margin:0;padding:0}
  html,body{width:1023px;height:1200px;overflow:hidden;background:var(--white)}
  .page{position:relative;width:1023px;height:1200px;font-family:'Open Sans',sans-serif}
  .abs{position:absolute}

  /* header */
  .call{left:711px;top:22px;font-family:'Open Sans',sans-serif;font-size:21px;color:#333}
  .call span{color:var(--accent)}
  .social{left:790px;top:54px;display:flex;gap:12px}
  .social i{display:block;width:28px;height:28px;border-radius:50%;background:var(--icon)}
  .brand{left:102px;top:72px;width:145px}
  .brand-name{font-family:'Open Sans',sans-serif;font-weight:700;font-size:50px;line-height:54px;color:var(--ink);text-align:center;letter-spacing:1px}
  .brand-tag{font-family:'Open Sans',sans-serif;font-size:14.5px;color:#333;margin-top:-2px;white-space:nowrap}
  .nav{left:264px;top:121px;width:642px;display:flex;justify-content:space-between;font-family:'Open Sans',sans-serif;font-weight:600;font-size:14.5px;color:var(--ink)}
  .nav a{color:inherit;text-decoration:none}
  .nav a:first-child{padding-left:16px}
  .nav a:last-child{padding-right:2px}
  .nav-rule{left:264px;top:144px;width:642px;height:4px;border:1px solid #cfcfcf;border-top:none;background:#f4f4f4}
  .nav-rule::before{content:"";position:absolute;left:0;top:-1px;width:80px;height:5px;background:var(--ink)}

  /* hero */
  .hero{left:0;top:172px;width:1023px;height:271px;background:var(--hero-band)}
  .hero-photo{left:102px;top:0;width:464px;height:271px;background:radial-gradient(ellipse at 40% 45%,#8a6664,#6f5453 70%,#5e4848)}
  .hero-panel{left:566px;top:0;width:339px;height:271px;background:linear-gradient(180deg,#151517,#232326);color:var(--white);padding:18px 12px 0 14px}
  .hero-panel h1{font-family:'Questrial',sans-serif;font-weight:400;font-size:26px;margin-bottom:18px}
  .hero-panel p{font-size:13.2px;line-height:15.4px;margin-bottom:15px}
  .btn{display:inline-block;background:var(--button);color:var(--white);font-family:'Open Sans',sans-serif;font-size:14.5px;line-height:20px;padding:2px 10px;border:1px solid #a58985}
  .hero-panel .btn{font-weight:700;margin-top:2px}

  /* services */
  .services{left:0;top:443px;width:1023px;height:448px;background:var(--section)}
  .services h2{position:absolute;left:102px;top:11px;font-family:'Questrial',sans-serif;font-weight:400;font-size:22px;color:#444}
  .card{position:absolute;top:52px;width:256px;height:373px;background:var(--card);border:1px solid var(--card-edge);padding:3px}
  .card-photo{height:173px}
  .card h3{font-family:'Questrial',sans-serif;font-weight:400;font-size:27px;color:var(--white);margin:26px 0 0 10px}
  .card p{font-size:13px;line-height:17px;color:#dedede;margin:13px 4px 0 10px}
  .card .btn{position:absolute;left:13px;top:330px;padding:2px 12px}

  /* footer */
  .footer{left:0;top:891px;width:1023px;height:262px;background:var(--footer);border-top:3px solid var(--footer-rule);color:var(--footer-text)}
  .footer h4{font-family:'Questrial',sans-serif;font-weight:400;font-size:16px}
  .newsletter{position:absolute;left:102px;top:22px;width:187px}
  .newsletter p{font-size:10.6px;line-height:12.5px;margin-top:12px}
  .field{display:block;height:30px;background:var(--field);border:1px solid #9a9a9a;margin-top:10px;padding:6px 9px;font-weight:700;font-size:12px;color:var(--white)}
  .field + .field{margin-top:8px}
  .submit{display:inline-block;margin-top:12px;background:linear-gradient(#1d8cb1,#0f5f7b);color:var(--white);font-size:13px;padding:2px 23px}
  .testimonials{position:absolute;left:306px;top:22px;width:395px}
  .quote{font-size:13.2px;line-height:15.4px;color:var(--muted);margin-top:13px;padding-left:2px;padding-right:12px}
  .quote + .author + .quote{margin-top:12px}
  .author{text-align:right;font-style:italic;font-weight:700;font-size:13px;color:var(--white);margin-top:6px}
  .contact{position:absolute;left:716px;top:12px;width:189px;text-align:right;font-family:'Questrial',sans-serif;font-size:15px;line-height:17px}
  .contact-head{display:flex;align-items:flex-end;justify-content:space-between;border-bottom:1px solid var(--accent);padding-bottom:2px;margin-bottom:16px}
  .contact-head h4{font-size:16px;margin-bottom:4px}
  .contact .line{display:flex;justify-content:flex-end;align-items:flex-start;gap:2px}
  .contact .line svg{flex:none;margin-top:-2px}
  .contact .gap{margin-top:12px}

  .bottom-nav{left:0;top:1153px;width:1023px;height:47px;background:var(--bar);font-size:13.5px;color:var(--white)}
  .bottom-nav span{position:absolute;top:14px}
</style>
</head>
<body>
<div class="page">

  <div class="abs call"><span>CALL</span> 1300 555 010</div>
  <div class="abs social" aria-label="Social links"><i></i><i></i><i></i></div>

  <div class="abs brand">
    <div class="brand-name">PRK</div>
    <div class="brand-tag">Your logo goes here</div>
  </div>

  <nav class="abs nav">
    <a href="#">Home</a><a href="#">Products</a><a href="#">Our Services</a><a href="#">Our Projects</a><a href="#">About Us</a><a href="#">Contact Us</a>
  </nav>
  <div class="abs nav-rule"></div>

  <section class="abs hero">
    <div class="abs hero-photo" role="img" aria-label="Close view of a glossy polished floor reflecting ceiling lights"></div>
    <div class="abs hero-panel">
      <h1>Welcome to PRK</h1>
      <p>PRK is a specialty contractor in fireproofing, epoxy flooring, terrazzo, poured floors and polished concrete. We are the largest specialty flooring healthcare contractor in the south east, trusted on hospitals and clinics.</p>
      <p>We also install fire caulking that keeps every wall and floor opening sealed, safe and fully up to code.</p>
      <span class="btn">Learn More</span>
    </div>
  </section>

  <section class="abs services">
    <h2>What we do</h2>

    <article class="card" style="left:102px">
      <div class="card-photo" role="img" aria-label="Glossy grey epoxy floor in a hallway" style="background:linear-gradient(160deg,#7d7d7d,#c4c4c4 50%,#8f8f8f)"></div>
      <h3>Epoxy flooring</h3>
      <p>Seamless, hygienic epoxy systems for hospital corridors, labs and clinics that need a tough floor.</p>
      <span class="btn">Learn More</span>
    </article>

    <article class="card" style="left:375px">
      <div class="card-photo" role="img" aria-label="Speckled terrazzo floor and staircase" style="background:linear-gradient(180deg,#ddd9d2,#c6b8a8 55%,#b3a08d)"></div>
      <h3>Terrazo flooring</h3>
      <p>Poured terrazzo with lasting colour and shine for busy lobbies, stairs and patient areas.</p>
      <span class="btn">Learn More</span>
    </article>

    <article class="card" style="left:648px">
      <div class="card-photo" role="img" aria-label="Polished concrete floor in a large bright hall" style="background:linear-gradient(180deg,#eceee6,#aeae98 50%,#6f6e58)"></div>
      <h3>Polished concrete</h3>
      <p>Poured and polished concrete floors for large halls and care spaces, bright and low upkeep.</p>
      <span class="btn">Learn More</span>
    </article>
  </section>

  <footer class="abs footer">
    <div class="newsletter">
      <h4>Newsletter</h4>
      <p>Sign up here to receive regular e-newsletter. Please note you will only be added to the list if a full name is submitted.</p>
      <span class="field">Email</span>
      <span class="field">Name</span>
      <span class="submit">Submit</span>
    </div>

    <div class="testimonials">
      <h4>Testimonials</h4>
      <p class="quote">PRK handled the fireproofing and fire caulking across our new hospital wing. The crew was on time, kept the site clean and every inspection passed first time.</p>
      <p class="author">Clara D.</p>
      <p class="quote">Our clinic needed new epoxy and terrazzo floors while staying open to patients. PRK worked in phases around us and the finish still looks brand new.</p>
      <p class="author">Peter L.</p>
    </div>

    <div class="contact">
      <div class="contact-head">
        <svg width="64" height="48" viewBox="0 0 64 48" aria-hidden="true">
          <path d="M4 18 L32 2 L60 18 L60 46 L4 46 Z" fill="#e8eef2"/>
          <rect x="12" y="8" width="40" height="26" fill="#ffffff"/>
          <path d="M4 18 L32 36 L60 18 L60 46 L4 46 Z" fill="#cfd8de"/>
          <path d="M4 46 L28 30 M60 46 L36 30" stroke="#aab6be" stroke-width="1.5"/>
          <circle cx="32" cy="20" r="8" fill="none" stroke="#1b8fb3" stroke-width="2.5"/>
        </svg>
        <h4>Contact details</h4>
      </div>
      <div class="line">18 Harbour Lane
        <svg width="12" height="12" viewBox="0 0 12 12" aria-hidden="true"><path d="M1 6 L6 1 L11 6 L9.5 6 L9.5 11 L2.5 11 L2.5 6 Z" fill="#fff"/></svg></div>
      <div>Westbrook&nbsp;&nbsp;&nbsp;</div>
      <div>South Riverside&nbsp;&nbsp;&nbsp;</div>
      <div>RV12 4QT&nbsp;&nbsp;&nbsp;</div>
      <div class="line gap">000-000-0000
        <svg width="12" height="12" viewBox="0 0 12 12" aria-hidden="true"><path d="M1 5 Q6 0 11 5 L9 6 L8 4.5 L4 4.5 L3 6 Z M3 7 L9 7 L10 11 L2 11 Z" fill="#fff"/></svg></div>
      <div class="line">www.prkfloors.example
        <svg width="12" height="12" viewBox="0 0 12 12" aria-hidden="true"><circle cx="6" cy="6" r="4.5" fill="none" stroke="#fff" stroke-width="1.2"/><path d="M1.5 6 H10.5 M6 1.5 V10.5" stroke="#fff" stroke-width="1"/></svg></div>
    </div>
  </footer>

  <nav class="abs bottom-nav">
    <span style="left:161px">Home</span>
    <span style="left:241px">Products</span>
    <span style="left:345px">Our Services</span>
    <span style="left:475px">Our Projects</span>
    <span style="left:606px">About Us</span>
    <span style="left:709px">Contact Us</span>
  </nav>

</div>
</body>
</html>
```